Banner Ad Design Project

Hello,

I need 2 banner designs for advertising on zarvio promoline. Each design must be declined in the following format :

- 300 x 50 Leaderboard pour mobiles
- 468 x 60 Bannière
- 728 x 90 Leaderboard
- 250 x 250 Carré
- 200 x 200 Petit carré
- 336 x 280 Grand rectangle
- 300 x 250 Rectangle intégré
- 120 x 600 Skyscraper
- 160 x 600 Skyscraper large

The banners are to promote an "home exchange" site : http://www.nestrotate.example

Here are the 2 texts that must appear on the banners:
- Say "bye bye" to hotel bill! Stay for free with NestRotate!
- Travel worldwide for free with NestRotate!

Target Market(s)

English customer world wide

Industry/Entity Type

Advertising

Requirements
Must have
• The name "NestRotate" must appear on each banner
The banner must have a look and feel similar of the website http://www.nestrotate.example

```html
<!DOCTYPE html>
<html lang="en">
<head>
<meta charset="utf-8">
<title>NestRotate banner set</title>
<link href="https://fonts.googleapis.com/css2?family=PT+Sans:wght@400;700&display=swap" rel="stylesheet">
<style>
  :root {
    --navy: #2b5b95;
    --bright-blue: #2a72d4;
    --green: #78b82a;
    --band-top: #6aa6e0;
    --band-mid: #3b7bc4;
    --band-bottom: #2a5d9f;
    --caption: #5a5a5a;
    --paper: #ffffff;
    --bg-light: #ffffff;
    --bg-dark: #d6d6d6;
  }
  * { margin: 0; padding: 0; box-sizing: border-box; }
  html, body { width: 1128px; height: 1200px; overflow: hidden; }
  body {
    position: relative;
    font-family: "PT Sans", Arial, sans-serif;
    font-weight: 700;
    background: radial-gradient(ellipse at 40% 40%, var(--bg-light) 0%, #f1f1f1 45%, var(--bg-dark) 100%);
  }
  .banner {
    position: absolute;
    background: var(--paper);
    border-radius: 8px;
    overflow: hidden;
    box-shadow: 0 8px 18px rgba(0,0,0,0.35);
  }
  .line {
    position: absolute;
    left: 0; right: 0;
    text-align: center;
    white-space: nowrap;
    line-height: 1;
  }
  .accent { color: var(--green); }
  .brand-band {
    position: absolute;
    left: 0; right: 0;
    display: flex;
    align-items: center;
    justify-content: center;
    background: linear-gradient(to bottom, var(--band-top) 0%, var(--band-mid) 50%, var(--band-bottom) 100%);
  }
  .brand-name {
    color: #ffffff;
    font-weight: 700;
    line-height: 1;
  }
  .divider {
    position: absolute;
    height: 3px;
    background: var(--navy);
  }
  .caption {
    position: absolute;
    font-size: 28px;
    color: var(--caption);
    text-align: center;
    width: 200px;
  }

  /* 250x250 square */
  .square { left: 141px; top: 92px; width: 457px; height: 455px; color: var(--navy); }
  .square .line { font-size: 64px; }
  .square .divider { left: 20px; right: 20px; top: 186px; }
  .square .brand-band { bottom: 0; height: 84px; }
  .square .brand-name { font-size: 50px; }

  /* 300x50 mobile leaderboard */
  .mobile { left: 95px; top: 911px; width: 549px; height: 94px; border-radius: 6px; color: var(--navy); }
  .mobile .line { top: 12px; font-size: 31px; }
  .mobile .brand-band { bottom: 0; height: 48px; }
  .mobile .brand-name { font-size: 34px; }

  /* 160x600 wide skyscraper */
  .skyscraper { left: 752px; top: 37px; width: 293px; height: 1102px; border-radius: 6px; color: var(--bright-blue); }
  .skyscraper .top-band { top: 0; height: 80px; }
  .skyscraper .brand-name { font-size: 36px; }
  .skyscraper .line { font-size: 60px; }
  .skyscraper .line.huge { font-size: 124px; }
  .skyscraper .divider { left: 22px; right: 22px; top: 501px; height: 3px; background: var(--bright-blue); }
  .free-orb {
    position: absolute;
    left: 32px; top: 614px;
    width: 228px; height: 228px;
    border-radius: 50%;
    background: radial-gradient(circle at 50% 30%, #3f8ee6 0%, #1d5fb8 50%, #0e3a7c 100%);
    box-shadow: 0 6px 10px rgba(0,0,0,0.3);
    display: flex; align-items: center; justify-content: center;
    color: var(--green);
    font-size: 96px;
  }
  .skyscraper .bottom-band { left: 6px; right: 6px; top: 982px; height: 56px; border-radius: 4px; }
  .skyscraper .bottom-band .brand-name { font-size: 33px; }
</style>
</head>
<body>

  <section class="banner square" aria-label="250 by 250 banner">
    <div class="line" style="top:22px">Say "<span class="accent">bye bye</span>"</div>
    <div class="line" style="top:100px">to hotel bill!</div>
    <div class="divider"></div>
    <div class="line" style="top:214px">Stay for <span class="accent">free</span></div>
    <div class="line" style="top:296px">with</div>
    <div class="brand-band"><span class="brand-name">NestRotate</span></div>
  </section>
  <div class="caption" style="left:270px; top:583px">250x250</div>

  <section class="banner mobile" aria-label="300 by 50 banner">
    <div class="line">Travel worldwide for <span class="accent">FREE</span> with</div>
    <div class="brand-band"><span class="brand-name">NestRotate</span></div>
  </section>
  <div class="caption" style="left:270px; top:1044px">300x50</div>

  <section class="banner skyscraper" aria-label="160 by 600 banner">
    <div class="brand-band top-band"><span class="brand-name">NestRotate</span></div>
    <div class="line" style="top:142px">Say</div>
    <div class="line accent" style="top:208px">"bye bye"</div>
    <div class="line" style="top:278px">to hotel</div>
    <div class="line huge" style="top:354px">bill!</div>
    <div class="divider"></div>
    <div class="line" style="top:530px">Stay for</div>
    <div class="free-orb">free</div>
    <div class="line" style="top:878px">with</div>
    <div class="brand-band bottom-band"><span class="brand-name">NestRotate</span></div>
  </section>
  <div class="caption" style="left:798px; top:1156px">160x600</div>

</body>
</html>
```